Promotional poster for a vintage motorcycle show.

Vertically oriented, based on 11 x 17 inch proportions

Though not to the exclusion of other design concepts, stylistically perhaps something evoking a vintage (early-mid 20th century) 2-3 color silk screen style event poster.

In addition to some sort of eyecatching, vintage / antique motorbike oriented graphic (preferably not Corwin Baxley based), the poster should include the following text and info:

3rd Annual Milo Quenby Vintage Motorcycle Show
Bordentown City, N.J.
October 1st (rain date Oct. 2nd)
11am-4pm

Presented in conjunction with the 27th Annual Thistlewood Fair

For further info, or to register your pre-1992 bike contact:
Marty@wheelvaultex.com or 555-204-8913

Sponsored by:
UptownHallowmereGuildway.com
Wheelvaultex.com

Must have
• See above project description
Nice to have
• See above project describtion

```html
<!DOCTYPE html>
<html lang="en">
<head>
<meta charset="utf-8">
<title>3rd Annual Milo Quenby Vintage Motorcycle Show</title>
<link rel="stylesheet" href="https://fonts.googleapis.com/css2?family=Staatliches&family=Oswald:wght@500&family=Tinos:wght@700&display=swap">
<style>
  :root {
    --backdrop: #f3ddb3;
    --paper-light: #dcc089;
    --paper-mid: #c49a5c;
    --paper-dark: #8d6131;
    --title-red: #a52a1a;
    --title-orange: #c8501c;
    --ink-brown: #5a3622;
    --ink-dark: #432716;
    --bike-dark: #3a2617;
    --bike-mid: #7a5430;
  }
  html, body { margin: 0; padding: 0; overflow: hidden; }
  body { width: 777px; height: 1200px; background: var(--backdrop); }
  .poster { position: relative; width: 777px; height: 1200px; overflow: hidden; background: var(--backdrop); }
  .parchment { position: absolute; left: 0; top: 0; width: 777px; height: 1200px; }
  .bike-photo {
    position: absolute; left: 300px; top: 378px; width: 424px; height: 700px;
    background: radial-gradient(ellipse at 55% 45%, var(--bike-mid) 0%, var(--bike-dark) 55%, rgba(58,38,23,0) 75%);
    border-radius: 40% 40% 30% 30%;
    opacity: .9;
  }
  .headline {
    position: absolute; left: 0; width: 800px; text-align: center;
    font-family: "Staatliches", sans-serif; color: var(--title-red);
    font-size: 46px; line-height: 1; letter-spacing: 1.5px;
    background: linear-gradient(180deg, var(--title-red) 40%, var(--title-orange) 100%);
    -webkit-background-clip: text; background-clip: text; -webkit-text-fill-color: transparent;
  }
  .headline-1 { top: 128px; }
  .headline-2 { top: 177px; }
  .info { position: absolute; left: 0; width: 800px; text-align: center; font-family: "Staatliches", sans-serif; color: var(--ink-brown); line-height: 1; }
  .info-place { top: 238px; font-size: 33px; letter-spacing: 1px; }
  .info-date { top: 280px; font-size: 26px; }
  .info-time { top: 322px; font-size: 34px; }
  .partner-note {
    position: absolute; left: 92px; top: 506px; margin: 0;
    font-family: "Staatliches", sans-serif; color: var(--ink-dark);
    font-size: 44px; line-height: 44px; letter-spacing: 1px;
  }
  .sponsors {
    position: absolute; left: 51px; top: 912px; margin: 0;
    font-family: "Oswald", sans-serif; font-weight: 500; color: var(--ink-dark);
    font-size: 18px; line-height: 33px; letter-spacing: -0.3px;
  }
  .register {
    position: absolute; left: 326px; top: 1112px; margin: 0;
    font-family: "Tinos", serif; font-weight: 700; color: var(--ink-brown);
    font-size: 14.5px; line-height: 19px;
  }
</style>
</head>
<body>
<main class="poster">
  <svg class="parchment" viewBox="0 0 777 1200" role="img" aria-label="Aged torn parchment sheet">
    <defs>
      <radialGradient id="paperTone" cx="45%" cy="40%" r="75%">
        <stop offset="0" stop-color="#e3c994"/>
        <stop offset=".6" stop-color="#cfa869"/>
        <stop offset="1" stop-color="#946634"/>
      </radialGradient>
    </defs>
    <path fill="url(#paperTone)" d="M26 42 L120 34 L210 40 L300 30 L420 38 L520 32 L640 40 L720 34 L748 60 L740 140 L750 230 L738 330 L746 430 L736 540 L748 650 L738 760 L746 870 L736 980 L746 1080 L740 1150 L700 1166 L600 1160 L500 1168 L380 1158 L260 1166 L150 1158 L60 1164 L34 1140 L40 1040 L28 940 L38 840 L30 720 L40 600 L30 480 L38 360 L28 250 L36 140 Z"/>
  </svg>

  <div class="bike-photo" role="img" aria-label="Sepia photograph of a vintage motorcycle seen from the front"></div>

  <div class="headline headline-1">3rd Annual Milo Quenby</div>
  <div class="headline headline-2">Vintage Motorcycle Show</div>

  <div class="info info-place">Bordentown City, N.J.</div>
  <div class="info info-date">October 1st (rain date Oct. 2nd)</div>
  <div class="info info-time">11am-4pm</div>

  <p class="partner-note">Presented in<br>conjunction<br>with the<br>27th Annual<br>Thistlewood<br>Fair</p>

  <p class="sponsors">Sponsored by:<br>UptownHallowmereGuildway.com<br>Wheelvaultex.com</p>

  <p class="register">For further info, or to register your pre-1992 bike<br>contact: Marty@wheelvaultex.com or 555-204-8913</p>
</main>
</body>
</html>
```